Gaming "Ember Tonic" Energy Drink CAN Design

Energy Drink called "Ember Tonic" which should include the classic Health Potions out of a video game like, Morvath, Realm of Ironvale, Crystal Odyssey, Stone Banners, Towers and Tempests and so on. Our Products is focused on gamers, geeks and nerds. DESIGN INFORMATION We want to have a design that fits the style of health potions we are looking for of a video game. The main color should be RED, which is the usual color for a Ember Tonic in a video game. The word "Ember Tonic" has become to be visible on the product foremost.
Updates

Langsam um Feedback zu geben

Target Market(s)

Gamers geeks and nerds

Font styles to use
Serif
Sans Serif
Decorative
Script

Colors
ec1f27

Requirements
Must have
• The Color Red has to be dominant, as the Ember Tonic is in a Video Game is Red
Nice to have
• Something that resembles a Ember Tonic out of a game like: Morvath, Realm of Ironvale, Crystal Odyssey

```html
<!DOCTYPE html>
<html lang="de">
<head>
<meta charset="utf-8">
<title>Ember Tonic – Dosenetikett</title>
<link rel="stylesheet" href="https://fonts.googleapis.com/css2?family=Cinzel:wght@700;900&family=Roboto+Condensed:wght@400;700&display=swap">
<style>
  :root {
    --stage: #eeeeee;
    --label-core: #6e1d10;
    --label-edge: #260605;
    --potion-red: #ec1f27;
    --title-red: #f2343b;
    --flame-deep: #d8361a;
    --flame-mid: #f47a1c;
    --flame-light: #fcc340;
    --ink-light: #ffffff;
    --ink-soft: #f3e6e2;
    --orb-rim: #c9a24a;
    --pill: #111111;
  }
  * { box-sizing: border-box; margin: 0; padding: 0; }
  html, body { width: 858px; height: 1200px; overflow: hidden; }
  body { background: var(--stage); position: relative; font-family: "Roboto Condensed", sans-serif; }

  .label {
    position: absolute; left: 29px; top: 301px; width: 800px; height: 598px;
    overflow: hidden;
    background: radial-gradient(ellipse at 62% 55%, var(--label-core) 0%, #4a100a 45%, var(--label-edge) 100%);
  }
  .flames { position: absolute; inset: 0; width: 800px; height: 598px; }

  .info { position: absolute; left: 36px; color: var(--ink-soft); font-size: 8px; line-height: 11px; text-transform: uppercase; }
  .info strong { color: var(--ink-light); font-weight: 700; }
  .ingredients { top: 35px; width: 216px; }

  .nutrition { position: absolute; left: 35px; top: 166px; width: 216px; border: 1.5px solid var(--ink-light); color: var(--ink-soft); font-size: 8px; line-height: 11.2px; text-transform: uppercase; }
  .nutrition-group { padding: 2px 4px; }
  .nutrition-group + .nutrition-group { border-top: 1.5px solid var(--ink-light); }
  .row { display: flex; justify-content: space-between; }
  .row.head { font-weight: 700; color: var(--ink-light); }
  .row .sub { padding-left: 8px; }
  .row .c2 { width: 60px; text-align: right; }
  .row .c3 { width: 46px; text-align: right; }
  .row .vals { display: flex; }

  .handling { top: 371px; width: 140px; }
  .handling p + p { margin-top: 5px; }
  .batch-box { position: absolute; left: 177px; top: 371px; width: 73px; height: 172px; background: var(--ink-light); }
  .volume { position: absolute; left: 180px; top: 555px; color: var(--ink-light); font-size: 17px; font-weight: 700; letter-spacing: -0.3px; }

  .brand { position: absolute; left: 341px; top: 60px; width: 360px; text-align: center; color: var(--title-red); font-family: "Cinzel", serif; font-weight: 900; line-height: 0.95; }
  .brand-line { display: block; font-size: 72px; letter-spacing: 1px; }
  .tagline { position: absolute; left: 341px; top: 236px; width: 360px; text-align: center; color: var(--ink-light); font-family: "Cinzel", serif; font-weight: 700; font-size: 13px; letter-spacing: 4px; }

  .orb { position: absolute; left: 395px; top: 315px; width: 268px; height: 268px; border-radius: 50%;
    border: 3px solid var(--orb-rim);
    background: radial-gradient(circle at 50% 78%, var(--potion-red) 0%, #a8141a 38%, #5a1a12 62%, #3a1410 100%); }
  .orb-text { position: absolute; left: 0; width: 100%; text-align: center; color: #e8d6c4; font-family: "Cinzel", serif; font-weight: 700; font-size: 15px; letter-spacing: 4px; }
  .orb-text.first { top: 65px; }
  .orb-text.second { top: 94px; }
  .orb-volume { position: absolute; left: 101px; top: 184px; width: 62px; height: 24px; border-radius: 12px; background: var(--pill); color: var(--ink-light); font-family: "Cinzel", serif; font-weight: 700; font-size: 11px; letter-spacing: 2px; line-height: 24px; text-align: center; }
</style>
</head>
<body>
  <section class="label" aria-label="Ember Tonic Dosenetikett, abgewickelt">
    <svg class="flames" viewBox="0 0 800 598" role="img" aria-label="Lodernde Flammen an den Rändern des Etiketts">
      <defs>
        <linearGradient id="flameGrad" x1="0" y1="0" x2="1" y2="1">
          <stop offset="0" stop-color="var(--flame-light)"/>
          <stop offset="0.5" stop-color="var(--flame-mid)"/>
          <stop offset="1" stop-color="var(--flame-deep)"/>
        </linearGradient>
      </defs>
      <path d="M0 0 H140 C120 20 90 25 60 30 C30 36 20 60 0 80 Z" fill="url(#flameGrad)"/>
      <path d="M800 0 V598 H600 C640 560 700 560 720 520 C690 470 740 440 730 400 C760 370 780 330 760 300 C740 270 760 230 780 200 C800 170 760 130 770 90 C780 50 760 20 800 0 Z" fill="url(#flameGrad)" opacity="0.92"/>
      <path d="M800 300 C770 340 760 380 780 420 C760 470 720 500 700 540 C690 570 670 590 650 598 H800 Z" fill="var(--flame-light)" opacity="0.55"/>
    </svg>

    <div class="info ingredients">
      <p><strong>Energy Drink – Pfandfrei</strong></p>
      <p><strong>Erhöhter Koffeingehalt (32mg/100ml)</strong></p>
      <p><strong>Zutaten:</strong> Molkenerzeugnis*, Wasser, Zucker, Säuerungsmittel E330, Kohlensäure, Säureregulatoren: E331, E332; Karamellisierter Zucker, Aroma, Glukuronolakton (0,04%), Taurin (0,04%), Koffein (0,03%), Inosit (0,02%), Vitamine: Niacin, Pantothensäure, Vitamin B6, Vitamin B12; Farbstoffe: E150d, E101</p>
    </div>

    <div class="nutrition">
      <div class="nutrition-group">
        <div class="row head"><span>Nährwerte</span><span>In 100ml</span></div>
        <div class="row"><span>Brennwert</span><span>198 kJ / 47 kcal</span></div>
        <div class="row"><span>Fett</span><span>0 g</span></div>
        <div class="row"><span class="sub">davon gesättigte Fettsäuren</span><span>0 g</span></div>
        <div class="row"><span>Kohlenhydrate</span><span>11,1 g</span></div>
        <div class="row"><span class="sub">davon Zucker</span><span>10,9 g</span></div>
        <div class="row"><span>Eiweiss</span><span>0 g</span></div>
        <div class="row"><span>Salz</span><span>&lt; 0,1 g</span></div>
      </div>
      <div class="nutrition-group">
        <div class="row head"><span>Vitamine</span><span class="vals"><span class="c2">In 100ml</span><span class="c3">% NRV**</span></span></div>
        <div class="row"><span>Niacin</span><span class="vals"><span class="c2">7,04 mg</span><span class="c3">44%</span></span></div>
        <div class="row"><span>Vitamin B6</span><span class="vals"><span class="c2">1,4 mg</span><span class="c3">100%</span></span></div>
        <div class="row"><span>Vitamin B12</span><span class="vals"><span class="c2">5,0 µg</span><span class="c3">200%</span></span></div>
        <div class="row"><span>Pantothensäure</span><span class="vals"><span class="c2">1,98 mg</span><span class="c3">33%</span></span></div>
      </div>
      <div class="nutrition-group">
        <div class="row"><span>* Enthält ein Milcherzeugnis</span></div>
        <div class="row"><span>**% der Nährstoffbezugswerte</span></div>
      </div>
    </div>

    <div class="info handling">
      <p>Gekühlt trinken<br>Pasteurisiert</p>
      <p>In moderaten Mengen konsumieren.<br>Für Kinder und Schwangere oder stillende Frauen nicht empfohlen.</p>
      <p><strong>Hergestellt in Österreich</strong><br>von Kesselgrund Production &amp; Development GmbH<br>Für XXXXXXXXXXXXXXX<br>XXXXXXXXXXXXXXXXXX<br>XXXXXXXX</p>
      <p>Mindestens haltbar bis: siehe Dosenboden</p>
    </div>
    <div class="batch-box" aria-label="Feld für Chargennummer"></div>
    <div class="volume">℮250ml</div>

    <h1 class="brand"><span class="brand-line">EMBER</span><span class="brand-line">TONIC</span></h1>
    <p class="tagline">DELICIOUS UNBOUND ENERGY</p>

    <div class="orb" role="img" aria-label="Glaskugel mit brodelndem roten Trank">
      <p class="orb-text first">INSTANT ENERGY</p>
      <p class="orb-text second">CAFFEINE FREE</p>
      <span class="orb-volume">300ML</span>
    </div>
  </section>
</body>
</html>
```